Top International Talent Management Needs creative business card design

We manage actors careers and book them liaising and promoting their profiles internationally through Casting Directors, Producers, Directors, Publicists etc. We need clearly visable contact details but with a design that reflects our status and creativity of TV, Feature Film industry. Our logo is attached and needs to relate and our website is www.quillbrookstagefolk.com
No flame designs please but please incorporate logo colours.

Target Market(s)

Clients

Industry/Entity Type

Film Production

Contact Information for Business Card

Director Rosalind Pettigrew
Suite D, Building 7, Harbourlight Lots Australia, Wren Flats, Sydney, NSW 2048

Font styles to use
Sans Serif

Colors
ec1f27

Requirements
Nice to have
• Colours should relate to logo attached and type can relate again to type in the logo design.
Should not have
• No Flames designs and best to be not too obvious with the film designs eiither. Needs to be more creative and modern

```html
<!DOCTYPE html>
<html lang="en">
<head>
<meta charset="utf-8">
<title>Quillbrook Stagefolk – Business Card</title>
<link rel="stylesheet" href="https://fonts.googleapis.com/css2?family=Open+Sans:wght@400;600;700&display=swap">
<style>
  :root {
    --page-bg: #e7e4e1;
    --card-top: #f4f3f2;
    --card-bottom: #dedbd8;
    --brand-red: #c4222a;
    --brand-red-dark: #8c1016;
    --name-red: #8e1a20;
    --ink: #2c2c2c;
    --divider: #6b6b6b;
    --marker: #262626;
  }
  * { box-sizing: border-box; margin: 0; padding: 0; }
  html, body {
    width: 1200px; height: 970px; overflow: hidden;
    background: var(--page-bg);
    font-family: "Open Sans", Arial, sans-serif;
  }
  .card {
    position: absolute; left: 100px; top: 199px;
    width: 1000px; height: 572px;
    background: linear-gradient(170deg, var(--card-top), var(--card-bottom));
    border-radius: 30px 4px 30px 4px;
    box-shadow: 0 14px 40px rgba(0,0,0,0.18);
    overflow: hidden;
  }
  .brand {
    position: absolute; left: 40px; top: 260px;
    font-size: 38px; font-weight: 700; color: var(--brand-red);
    letter-spacing: 0.5px; white-space: nowrap;
  }
  .divider {
    position: absolute; left: 503px; top: 150px;
    width: 1.5px; height: 222px; background: var(--divider);
  }
  .details { position: absolute; left: 537px; top: 98px; color: var(--ink); }
  .name { font-size: 41px; font-weight: 700; color: var(--name-red); line-height: 1.1; white-space: nowrap; }
  .role { font-size: 23px; line-height: 1.3; margin-bottom: 18px; }
  .address { font-size: 21px; line-height: 1.4; margin-bottom: 18px; white-space: nowrap; }
  .contacts { list-style: none; font-size: 21px; line-height: 33px; }
  .contacts li { display: flex; align-items: center; gap: 10px; white-space: nowrap; }
  .contacts svg { width: 18px; height: 18px; fill: var(--brand-red); flex: none; }
  .band {
    position: absolute; left: 0; bottom: 0; width: 100%; height: 44px;
    background: linear-gradient(90deg, var(--brand-red-dark), var(--brand-red) 30%, var(--brand-red) 60%, var(--brand-red-dark));
  }
  .band-marker { position: absolute; left: 534px; bottom: 22px; width: 30px; height: 24px; }
</style>
</head>
<body>
  <div class="card">
    <div class="brand">Quillbrook Stagefolk</div>
    <div class="divider"></div>

    <div class="details">
      <div class="name">Rosalind Pettigrew</div>
      <div class="role">Director</div>
      <div class="address">Suite D, Building 7,<br>Harbourlight Lots Australia,<br>Wren Flats, Sydney, NSW 2048</div>
      <ul class="contacts">
        <li><svg viewBox="0 0 24 24" aria-hidden="true"><path d="M6.6 10.8a15 15 0 0 0 6.6 6.6l2.2-2.2c.3-.3.7-.4 1-.2 1.1.4 2.300.6 3.6.6.6 0 1 .4 1 1V20c0 .6-.4 1-1 1A17 17 0 0 1 3 4c0-.6.4-1 1-1h3.5c.6 0 1 .4 1 1 0 1.3.2 2.500.6 3.6.1.3 0 .7-.2 1z"/></svg>(02) 5550 7730</li>
        <li><svg viewBox="0 0 24 24" aria-hidden="true"><path d="M6 2h9l3 3v5H6zM3 11h18v8h-3v3H6v-3H3zm5 5v4h8v-4z"/></svg>(02) 5550 7731</li>
        <li><svg viewBox="0 0 24 24" aria-hidden="true"><path d="M7 1h10a2 2 0 0 1 2 2v18a2 2 0 0 1-2 2H7a2 2 0 0 1-2-2V3a2 2 0 0 1 2-2zm0 3v14h10V4zm5 15.5a1.2 1.2 0 1 0 0 2.4 1.2 1.2 0 0 0 0-2.4z"/></svg>0455 390 418</li>
        <li><svg viewBox="0 0 24 24" aria-hidden="true"><path d="M2 5h20v14H2zm2 2v.5l8 5 8-5V7zm0 2.8V17h16V9.8l-8 5z"/></svg>rosalind@quillbrookstagefolk.com</li>
        <li><svg viewBox="0 0 24 24" aria-hidden="true"><path d="M12 2a10 10 0 1 0 0 20 10 10 0 0 0 0-20zm6.9 9h-3a15 15 0 0 0-1.3-6A8 8 0 0 1 18.9 11zM12 4c.9 1.2 1.8 3.8 1.9 7h-3.8C10.2 7.8 11.1 5.2 12 4zM9.4 5a15 15 0 0 0-1.3 6h-3A8 8 0 0 1 9.4 5zM5.1 13h3a15 15 0 0 0 1.3 6 8 8 0 0 1-4.3-6zM12 20c-.9-1.2-1.8-3.8-1.9-7h3.8c-.1 3.2-1 5.8-1.9 7zm2.6-1a15 15 0 0 0 1.3-6h3a8 8 0 0 1-4.3 6z"/></svg>www.quillbrookstagefolk.com</li>
      </ul>
    </div>

    <div class="band"></div>
    <svg class="band-marker" viewBox="0 0 30 24" aria-hidden="true">
      <polygon points="2,2 28,2 15,22" fill="var(--marker)" stroke="#ffffff" stroke-width="2" stroke-linejoin="round"/>
    </svg>
  </div>
</body>
</html>
```